New LGBT Nightclub Crowdfunding Poster

We need it to read well for social media posts. All colors should look similar to Seattle’s Sports Teams color schemes.

The top should have: The logo prominently with the fans in the background photo. and then still center and important, "Coming soon!" "You can be part of the first in line for the amazing things happening". (The call to action is the purchase of these amazing deals for the first weekend open / passes. That should be clear).

```html
<!DOCTYPE html>
<html lang="en">
<head>
<meta charset="utf-8">
<title>The Encore — Coming Soon</title>
<link rel="stylesheet" href="https://fonts.googleapis.com/css2?family=Teko:wght@500;600;700&family=Montserrat:wght@400;500;700&display=swap">
<style>
  :root {
    --navy-deep: #0b1442;
    --navy: #14226a;
    --royal: #1d3aa6;
    --sky: #2aa9e1;
    --white: #ffffff;
    --silver: #dfe6ee;
    --wash: #2a3d7a;
  }
  * { margin: 0; padding: 0; box-sizing: border-box; }
  html, body { width: 868px; height: 1200px; overflow: hidden; background: var(--white); }
  .poster {
    position: relative;
    width: 868px;
    height: 1200px;
    overflow: hidden;
    font-family: "Montserrat", Arial, sans-serif;
    color: var(--white);
    background: var(--navy-deep);
  }
  .backdrop { position: absolute; inset: 0; width: 868px; height: 1200px; }

  .brand {
    position: absolute;
    left: 32px; top: 103px;
    width: 250px; height: 250px;
    border-radius: 50%;
    background: radial-gradient(circle at 50% 40%, var(--wash) 0%, #3c4f8c 55%, #c9cfdc 80%, #eef0f4 100%);
  }
  .brand-name {
    position: absolute;
    left: 32px; top: 196px;
    width: 250px;
    text-align: center;
    font-family: "Teko", "Arial Narrow", sans-serif;
    font-weight: 600;
    font-size: 46px;
    line-height: 40px;
    color: var(--white);
    text-transform: uppercase;
  }

  .headline {
    position: absolute;
    font-family: "Teko", "Arial Narrow", sans-serif;
    font-weight: 700;
    text-transform: uppercase;
    white-space: nowrap;
    transform-origin: center;
  }
  .headline-coming {
    left: 300px; top: 40px;
    width: 430px;
    text-align: center;
    font-size: 150px;
    line-height: 150px;
    color: var(--silver);
    text-shadow: 0 3px 0 #9aa7b6, 0 6px 8px rgba(0,0,0,0.35);
    transform: rotate(-5deg) skewX(-8deg);
  }
  .headline-soon {
    left: 330px; top: 155px;
    width: 480px;
    text-align: center;
    font-size: 210px;
    line-height: 200px;
    color: var(--navy);
    text-shadow: 2px 2px 0 var(--sky), 5px 6px 0 var(--navy-deep);
    transform: rotate(-5deg) skewX(-8deg);
  }

  .tagline {
    position: absolute;
    left: 120px; top: 362px;
    width: 620px;
    text-align: center;
    font-family: "Teko", "Arial Narrow", sans-serif;
    font-weight: 600;
    font-size: 42px;
    line-height: 38px;
    text-transform: uppercase;
    color: var(--white);
    transform: rotate(-5deg) skewX(-10deg);
  }

  .levels-title {
    position: absolute;
    left: 0; top: 510px;
    width: 868px;
    text-align: center;
    font-family: "Teko", "Arial Narrow", sans-serif;
    font-weight: 600;
    font-size: 58px;
    line-height: 60px;
    text-transform: uppercase;
    letter-spacing: 1px;
  }

  .levels { position: absolute; left: 0; top: 0; width: 868px; list-style: none; }
  .level {
    position: absolute;
    left: 0; width: 868px;
    display: flex;
    align-items: center;
  }
  .level-price {
    width: 140px;
    text-align: right;
    font-family: "Teko", "Arial Narrow", sans-serif;
    font-weight: 500;
    font-size: 38px;
    line-height: 38px;
    color: var(--sky);
    padding-top: 4px;
  }
  .level-detail {
    margin-left: 25px;
    width: 660px;
    font-size: 12.4px;
    line-height: 20px;
    font-weight: 500;
    text-transform: uppercase;
  }
  .divider {
    position: absolute;
    left: 28px; width: 816px;
    border-top: 1px dashed rgba(42,169,225,0.55);
  }

  .crowd {
    position: absolute;
    left: 0; top: 1020px;
    width: 868px; height: 180px;
    background: linear-gradient(180deg, rgba(45,60,190,0) 0%, rgba(45,60,190,0.55) 45%, #1a1f7a 100%);
  }

  .closing {
    position: absolute;
    left: 0; width: 868px;
    text-align: center;
    color: var(--white);
  }
  .closing-ask { top: 1042px; font-weight: 700; font-size: 22px; line-height: 30px; }
  .closing-pass { top: 1080px; font-weight: 400; font-size: 22px; line-height: 30px; color: #d6e6ff; }
  .closing-web { top: 1143px; font-weight: 400; font-size: 15px; line-height: 22px; }
</style>
</head>
<body>
<main class="poster">
  <svg class="backdrop" viewBox="0 0 868 1200" preserveAspectRatio="none" aria-hidden="true">
    <defs>
      <linearGradient id="panel-glow" x1="0" y1="0" x2="1" y2="1">
        <stop offset="0" stop-color="#0b1442"/>
        <stop offset="0.6" stop-color="#14226a"/>
        <stop offset="1" stop-color="#1d3aa6"/>
      </linearGradient>
    </defs>
    <rect x="0" y="0" width="868" height="1200" fill="url(#panel-glow)"/>
    <polygon points="0,0 868,0 868,297 0,388" fill="#ffffff"/>
    <polygon points="377,0 868,0 868,130 283,192" fill="#14226a"/>
    <polygon points="293,64 742,23 730,143 283,192" fill="#2aa9e1"/>
    <polygon points="0,388 868,297 868,422 0,496" fill="#2aa9e1"/>
    <line x1="0" y1="388" x2="868" y2="297" stroke="#14226a" stroke-width="4"/>
    <polygon points="590,446 868,420 868,432 560,452" fill="#ffffff"/>
    <line x1="0" y1="496" x2="868" y2="422" stroke="#14226a" stroke-width="3"/>
  </svg>

  <div class="brand" role="img" aria-label="Watercolour crowd of dancers with raised hands in a circle"></div>
  <div class="brand-name">The Encore</div>

  <h1 class="headline headline-coming">Coming</h1>
  <p class="headline headline-soon">Soon!</p>

  <p class="tagline">Be part of the newest chapter<br>in Seattle's LGBT nightlife history.</p>

  <h2 class="levels-title">Crowdfunding Levels</h2>

  <div class="crowd" role="img" aria-label="Silhouetted crowd with raised hands under blue stage light"></div>

  <ul class="levels">
    <li class="level" style="top:590px"><span class="level-price">$25</span><span class="level-detail">An opening Fri or Sat night Glitz general admission ticket to see an TDS superstar. Only 100 tickets are available per night.</span></li>
    <li class="level" style="top:654px"><span class="level-price">$50</span><span class="level-detail">An opening Fri or Sat seat to Glitz. Third-tier seating. Only 60 tickets are available per night.</span></li>
    <li class="level" style="top:726px"><span class="level-price">$75</span><span class="level-detail">An opening Fri or Sat middle-tier seat to a Glitz show featuring a surprise TDS superstar. Only 60 tickets are available per night.</span></li>
    <li class="level" style="top:797px"><span class="level-price">$100</span><span class="level-detail">An opening Fri or Sat night VIP ticket to Glitz featuring a secret TDS superstar. Only 60 tickets are available per night.</span></li>
    <li class="level" style="top:868px"><span class="level-price">$500</span><span class="level-detail">The Encore Pass. You can skip the line and don't have to pay a cover charge for 6 months. This doesn't include brunch shows and special events. Special Encore merch is included. 50 passes are available.</span></li>
    <li class="level" style="top:954px"><span class="level-price">$1000</span><span class="level-detail">The Encore Gold Pass. Skip the line and get free cover for the entire year. This doesn't include brunch shows and special events. Special Encore merch is included. 100 passes are available.</span></li>
  </ul>

  <div class="divider" style="top:647px"></div>
  <div class="divider" style="top:710px"></div>
  <div class="divider" style="top:784px"></div>
  <div class="divider" style="top:856px"></div>
  <div class="divider" style="top:939px"></div>

  <p class="closing closing-ask">Want more?</p>
  <p class="closing closing-pass">Ask about The Encore Elite Pass.</p>
  <p class="closing closing-web">www.theencoreseattle.com</p>
</main>
</body>
</html>
```